PawNook business card

Looking for a fun and cool biz card for a new company with patent pending products. I have products to help and protect dogs hearing. My colors are pantone blue and orange.
Updates

Please add tag line: Protect the ones you love...even your PawNooks!

Target Market(s)

Animal/Dog lovers!

Industry/Entity Type

Retail

Contact Information for Business Card

I'm looking for something simple yet fun with all the info included for biz cards

Colors
0555a3
f78f20

Requirements
Must have
• Logo
Nice to have
• name, website and email
Should not have
• phone number

```html
<!DOCTYPE html>
<html lang="en">
<head>
<meta charset="utf-8">
<title>PawNook business card</title>
<link rel="stylesheet" href="https://fonts.googleapis.com/css2?family=Montserrat:wght@600&family=Open+Sans:ital,wght@1,800&family=Questrial&display=swap">
<style>
  :root {
    --brand-orange: #fc4f00;
    --brand-blue: #0a3189;
    --paw-on-orange: #fd8656;
    --paw-on-blue: #4a67ad;
    --ink-navy: #1b2f5a;
    --card-text: #ffffff;
    --logo-dark: #8a2a00;
    --page: #ffffff;
  }
  * { margin: 0; padding: 0; box-sizing: border-box; }
  html, body { width: 1200px; height: 621px; overflow: hidden; background: var(--page); }
  .presentation { position: relative; width: 1200px; height: 621px; }

  .card {
    position: absolute;
    width: 523px;
    height: 296px;
    box-shadow: 0 2px 6px rgba(0,0,0,0.25);
    overflow: hidden;
    font-family: "Questrial", sans-serif;
    background: var(--brand-blue);
  }
  .card--front { left: 54px; top: 121px; }
  .card--back { left: 599px; top: 194px; }

  .front-panel { position: absolute; left: 0; top: 0; }

  .brand-name {
    position: absolute;
    font-family: "Questrial", sans-serif;
    white-space: nowrap;
    letter-spacing: 0.5px;
    line-height: 1;
  }
  .card--front .brand-name {
    left: 0; width: 254px; text-align: center;
    top: 121px; font-size: 40px; color: var(--logo-dark);
  }
  .website {
    position: absolute; left: 0; width: 254px; text-align: center;
    top: 177px; font-size: 15px; color: var(--logo-dark);
  }
  .paw { position: absolute; }
  .card--front .paw { left: 96px; top: 206px; }

  .holder-name {
    position: absolute; left: 277px; top: 22px;
    font-size: 31px; font-weight: 400; color: var(--card-text); white-space: nowrap;
  }
  .holder-name strong { font-family: "Montserrat", sans-serif; font-weight: 600; }
  .holder-role {
    position: absolute; left: 277px; top: 63px;
    font-family: "Montserrat", sans-serif; font-weight: 600;
    font-size: 11px; color: var(--card-text);
  }
  .contact-list { position: absolute; left: 277px; top: 143px; list-style: none; color: var(--card-text); font-size: 16.5px; }
  .contact-item { display: flex; line-height: 22px; }
  .contact-item + .contact-item { margin-top: 16px; }
  .contact-label { font-family: "Montserrat", sans-serif; font-weight: 600; font-size: 14px; width: 26px; }
  .tagline {
    position: absolute; left: 277px; top: 244px;
    font-size: 13px; line-height: 17px; color: var(--card-text);
  }

  .card--back .brand-name {
    left: 159px; top: 144px; font-size: 52px; color: var(--brand-orange);
  }
  .card--back .paw { left: 405px; top: 178px; }

  .feature-list {
    position: absolute; left: 660px; top: 83px;
    font-family: "Open Sans", sans-serif; font-style: italic; font-weight: 800;
    font-size: 19px; letter-spacing: 2.6px; line-height: 25px;
    color: var(--ink-navy); list-style: none;
  }
  .feature-list .continued { padding-left: 6px; }

  .side-label {
    position: absolute;
    font-family: "Open Sans", sans-serif; font-style: italic; font-weight: 800;
    font-size: 19px; letter-spacing: 3px; color: var(--ink-navy);
    transform: translateX(-50%); white-space: nowrap;
  }
  .side-label--front { left: 261px; top: 443px; }
  .side-label--back { left: 861px; top: 523px; }
</style>
</head>
<body>
<main class="presentation">

  <ul class="feature-list">
    <li>1.FULL EDITABLE</li>
    <li>2.FONTS GIVEN-AI, EPS, PDF,</li>
    <li class="continued">JPG, PNG,TIFF AVAILABLE</li>
  </ul>

  <section class="card card--front" aria-label="Business card front">
    <svg class="front-panel" width="523" height="296" viewBox="0 0 523 296" aria-hidden="true">
      <path fill="var(--brand-orange)"
        d="M0 0 H234 V52 C234 67 245 71 259 81 C269 89 272 95 272 109 V216 C272 230 269 236 259 244 C245 254 234 258 234 273 V296 H0 Z"/>
    </svg>

    <div class="brand-name">PawNook</div>
    <div class="website">www.pawnook.com</div>
    <svg class="paw" width="56" height="58" viewBox="0 0 56 58" role="img" aria-label="Paw print decoration">
      <ellipse cx="28" cy="31" rx="24" ry="24" fill="var(--paw-on-orange)"/>
    </svg>

    <h1 class="holder-name"><strong>Sam</strong> Rivera</h1>
    <p class="holder-role">owner</p>
    <ul class="contact-list">
      <li class="contact-item"><span class="contact-label">E:</span><span class="contact-value">sam.rivera@pawnook.com</span></li>
      <li class="contact-item"><span class="contact-label">O:</span><span class="contact-value">18 Maple Lane<br>Brookfield, NY 05410</span></li>
    </ul>
    <p class="tagline">Protect the ones you love...<br>even your PawNooks!</p>
  </section>

  <section class="card card--back" aria-label="Business card back">
    <div class="brand-name">PawNook</div>
    <svg class="paw" width="96" height="92" viewBox="0 0 96 92" role="img" aria-label="Large faint paw print decoration">
      <ellipse cx="48" cy="50" rx="40" ry="38" fill="var(--paw-on-blue)"/>
    </svg>
  </section>

  <p class="side-label side-label--front">FRONT SIDE</p>
  <p class="side-label side-label--back">BACK SIDE</p>

</main>
</body>
</html>
```